The Seeds Beneath Wintermoor Inc.

On one side have the business name. On the other side have contact information. This is an indoor cannabis cultivation business. It’s a new company in Sacramento ca. So we need a logo designed. The company is Called the seeds beneath wintermoor. We grow and distribute marijuana in California. We would like to see designers use the color green and communicate cultivation.

Target Market(s)

Networking

Contact Information for Business Card

Wade Tirrenbek: president
Phone: (916) 555-0173
Email: wade@theseedsbeneathwintermoor.net

Logo Text

Not sure if i want text or just an image created by designers.

Font styles to use
Script

Colors
000000
9bcb3c
fbfcf7
cadf82

Requirements
Nice to have
• A classic elegant professional card.

```html
<!DOCTYPE html>
<html lang="en">
<head>
<meta charset="utf-8">
<title>The Seeds Beneath Wintermoor Inc. — Business Card</title>
<link rel="stylesheet" href="https://fonts.googleapis.com/css2?family=Open+Sans:wght@400;700;800&display=swap">
<style>
  :root {
    --ink: #000000;
    --leaf: #9bcb3c;
    --leaf-soft: #cadf82;
    --paper: #fbfcf7;
    --backdrop: #3a3b38;
    --text-dark: #1a1a1a;
  }
  * { box-sizing: border-box; margin: 0; padding: 0; }
  html, body {
    width: 1200px; height: 824px; overflow: hidden;
    background: var(--backdrop);
    font-family: "Open Sans", Arial, sans-serif;
  }
  .stage {
    position: relative; width: 1200px; height: 824px;
    display: flex; align-items: center; justify-content: center; gap: 60px;
  }
  .card {
    width: 510px; height: 292px; position: relative;
    box-shadow: 0 12px 30px rgba(0,0,0,.45);
  }
  .card--front { background: var(--ink); display: flex; align-items: center; justify-content: center; }
  .card--back { background: var(--paper); }

  .wordmark { display: flex; align-items: center; gap: 14px; color: var(--leaf); font-weight: 800; }
  .wordmark__dot { width: 22px; height: 22px; border-radius: 50%; background: var(--leaf); flex: none; }
  .wordmark__name { line-height: 1.05; text-transform: lowercase; }
  .card--front .wordmark__name { font-size: 34px; }
  .card--back .wordmark { position: absolute; left: 34px; top: 96px; gap: 10px; }
  .card--back .wordmark__name { font-size: 21px; }
  .card--back .wordmark__dot { width: 14px; height: 14px; }

  .contact { position: absolute; left: 250px; top: 150px; color: var(--text-dark); }
  .contact__name { font-size: 20px; font-weight: 800; letter-spacing: .3px; }
  .contact__role { font-size: 11px; font-weight: 700; color: var(--leaf); margin: 1px 0 10px; }
  .contact__line { display: flex; align-items: center; gap: 9px; font-size: 12.5px; margin-bottom: 6px; }
  .contact__icon { width: 11px; height: 11px; flex: none; }
</style>
</head>
<body>
<main class="stage">
  <section class="card card--front" aria-label="Card front">
    <div class="wordmark">
      <span class="wordmark__dot"></span>
      <span class="wordmark__name">the seeds beneath<br>wintermoor</span>
    </div>
  </section>

  <section class="card card--back" aria-label="Card back">
    <div class="wordmark">
      <span class="wordmark__dot"></span>
      <span class="wordmark__name">the seeds beneath<br>wintermoor</span>
    </div>
    <div class="contact">
      <p class="contact__name">Wade Tirrenbek</p>
      <p class="contact__role">President</p>
      <p class="contact__line">
        <svg class="contact__icon" viewBox="0 0 12 12" aria-hidden="true"><path fill="var(--leaf)" d="M1 4c0-2 2-3 5-3s5 1 5 3v1H8V4H4v1H1zM3 6h6l1 5H2z"/></svg>
        (916) 555-0173
      </p>
      <p class="contact__line">
        <svg class="contact__icon" viewBox="0 0 12 12" aria-hidden="true"><rect x="0.5" y="2" width="11" height="8" fill="var(--leaf)"/><path d="M0.5 2.5 6 7l5.5-4.5" fill="none" stroke="var(--paper)" stroke-width="1"/></svg>
        wade@theseedsbeneathwintermoor.net
      </p>
    </div>
  </section>
</main>
</body>
</html>
```